Business Card for Industrial Distributor

We need a business card design for an industrial distributor. We sell machine parts for the manufacturing and oil industry. We would like the cards to look clean and modern but with a touch of industry.

Our colors are blue/white.

Please feel free to visit our website www.krovelmint.com

Target Market(s)

mexican manufacturers in the automobile/aerospace industry

Industry/Entity Type

Industrial

Colors
ffffff
0555a3

```html
<!DOCTYPE html>
<html lang="en">
<head>
<meta charset="utf-8">
<title>Krovelmint Business Card</title>
<link rel="stylesheet" href="https://fonts.googleapis.com/css2?family=Lato:wght@400;700;900&display=swap">
<style>
  :root {
    --brand-blue: #0555a3;
    --card-blue: #12599b;
    --white: #ffffff;
    --arc-grey: #9a9b9e;
    --stage: #3f3f3f;
  }
  * { margin: 0; padding: 0; box-sizing: border-box; }
  html, body { width: 1200px; height: 810px; overflow: hidden; }
  body {
    background: var(--stage);
    font-family: "Lato", Arial, sans-serif;
    position: relative;
  }
  .card {
    position: absolute;
    width: 540px;
    height: 310px;
    border-radius: 24px;
    overflow: hidden;
  }
  /* Back of card */
  .card-back {
    left: 80px; top: 110px;
    background: var(--card-blue);
    color: var(--white);
  }
  .card-back .brand {
    position: absolute;
    left: 0; right: 0; top: 118px;
    display: flex; align-items: center; justify-content: center; gap: 16px;
  }
  .brand-dot {
    width: 62px; height: 62px; border-radius: 50%;
    background: var(--white);
  }
  .card-back .brand-name {
    font-weight: 900; font-size: 58px; letter-spacing: -1px; line-height: 1;
  }
  .card-back .site {
    position: absolute; left: 0; right: 0; top: 250px;
    text-align: center; font-size: 14px; letter-spacing: .3px;
  }
  /* Front of card */
  .card-front {
    left: 580px; top: 390px;
    background: var(--card-blue);
  }
  .card-front .shape { position: absolute; inset: 0; }
  .card-front .brand {
    position: absolute; left: 14px; top: 98px; width: 290px;
    display: flex; flex-direction: column; align-items: center; gap: 12px;
  }
  .card-front .brand-dot {
    width: 60px; height: 60px;
    background: var(--brand-blue);
  }
  .card-front .brand-name {
    color: var(--brand-blue);
    font-weight: 900; font-size: 46px; letter-spacing: -1px; line-height: 1;
  }
  .person {
    position: absolute; right: 34px; top: 30px;
    text-align: right; color: var(--white);
  }
  .person-name { font-size: 24px; font-weight: 700; letter-spacing: .3px; }
  .person-title { font-size: 13px; margin-top: 2px; }
  .details {
    position: absolute; right: 26px; top: 150px;
    color: var(--white); font-size: 13px; text-align: right; line-height: 1.35;
  }
  .address { margin-bottom: 12px; }
  .line { display: flex; justify-content: flex-end; align-items: center; gap: 7px; }
  .line svg { width: 13px; height: 13px; flex: none; }
</style>
</head>
<body>
  <section class="card card-back">
    <div class="brand">
      <span class="brand-dot"></span>
      <span class="brand-name">Krovelmint</span>
    </div>
    <p class="site">www.krovelmint.com</p>
  </section>

  <section class="card card-front">
    <svg class="shape" viewBox="0 0 540 310" width="540" height="310">
      <path d="M0,0 L190,0 C290,30 335,150 318,310 L0,310 Z" fill="var(--white)"/>
      <path d="M190,0 C300,28 348,150 329,310 L318,310 C335,150 290,30 190,0 Z" fill="var(--arc-grey)"/>
    </svg>
    <div class="brand">
      <span class="brand-dot"></span>
      <span class="brand-name">Krovelmint</span>
    </div>
    <div class="person">
      <p class="person-name">Daniel Orrest</p>
      <p class="person-title">President &amp; CEO</p>
    </div>
    <div class="details">
      <p class="address">4280 Corvane Yard Rd,<br>Eastbridge, TX 78999</p>
      <p class="line">(555) 014 - 2290
        <svg viewBox="0 0 24 24"><path fill="#fff" d="M6.6 10.8a15 15 0 0 0 6.6 6.6l2.2-2.2c.3-.3.7-.4 1-.2 1.1.4 2.3.6 3.6.6.6 0 1 .4 1 1V20c0 .6-.4 1-1 1A17 17 0 0 1 3 4c0-.6.4-1 1-1h3.5c.6 0 1 .4 1 1 0 1.3.2 2.5.6 3.6.1.3 0 .7-.2 1z"/></svg>
      </p>
      <p class="line">(555) 014 - 2293
        <svg viewBox="0 0 24 24"><rect x="6" y="2" width="12" height="20" rx="2" fill="#fff"/><rect x="8" y="5" width="8" height="12" fill="var(--card-blue)"/></svg>
      </p>
      <p class="line">sales@krovelmint.com
        <svg viewBox="0 0 24 24"><rect x="2" y="5" width="20" height="14" fill="#fff"/><path d="M2 5l10 8 10-8" fill="none" stroke="var(--card-blue)" stroke-width="1.8"/></svg>
      </p>
      <p class="line">www.krovelmint.com
        <svg viewBox="0 0 24 24" fill="none" stroke="#fff" stroke-width="1.8"><circle cx="12" cy="12" r="9.5"/><ellipse cx="12" cy="12" rx="4" ry="9.5"/><path d="M2.5 12h19M4 7h16M4 17h16"/></svg>
      </p>
    </div>
  </section>
</body>
</html>
```